Movie poster for short film: TINFOIL

We need a creative, artistic, stylized poster design for our short film TINFOIL. We would like to see designs with graphics and bold colors more than photographs. The photographs we are posting are more for reference- you do not have to use them in the poster! We are looking for something clean and simple. The film is a drama so please don't make it funny. The mood of the film is thoughtful and introspective. Name of film should be in all caps. Things to include in the poster:
Name of film: TINFOIL
Velvet Harbor Pictures
Starring Marisa Calloway

Here is a brief plot synopsis: TINFOIL follows one night in the life of a rebellious young woman who breaks into a diner after hours with a can of spray paint. Her intentions change after she ends up discovering what's left of a love story.

The movie is somewhat experimental, set to music for part of it with no dialog. The whole movie takes place in an old fashioned diner.

Target Market(s)

Film festival attendees between the ages of 20-50

Industry/Entity Type

Movie

Font styles to use
Sans Serif

Requirements
Must have
• See project description above- also the film is somewhat dark in nature so please don't make it too 'happy' looking.

```html
<!DOCTYPE html>
<html lang="en">
<head>
<meta charset="utf-8">
<title>TINFOIL — Poster</title>
<link rel="stylesheet" href="https://fonts.googleapis.com/css2?family=Jost:wght@400;500&display=swap">
<style>
  :root {
    --ink: #000000;
    --paper: #ffffff;
    --gum-pink: #dd3594;
  }
  html, body {
    margin: 0;
    padding: 0;
    background: var(--ink);
    overflow: hidden;
  }
  .poster {
    position: relative;
    width: 960px;
    height: 1200px;
    background: var(--ink);
    color: var(--paper);
    font-family: "Jost", "Futura", sans-serif;
    overflow: hidden;
  }
  .presenter {
    position: absolute;
    top: 45px;
    left: 0;
    width: 100%;
    text-align: center;
    font-size: 17px;
    font-weight: 500;
    line-height: 20px;
    margin: 0;
  }
  .title {
    position: absolute;
    top: 94px;
    left: 84px;
    width: 797px;
    margin: 0;
    display: flex;
    justify-content: space-between;
    font-size: 128px;
    font-weight: 400;
    line-height: 1;
  }
  .title span { display: block; }
  .emblem {
    position: absolute;
    left: 61px;
    top: 248px;
    width: 838px;
    height: 838px;
  }
  .emblem circle { fill: var(--gum-pink); }
  .billing {
    position: absolute;
    left: 0;
    width: 100%;
    text-align: center;
    margin: 0;
  }
  .billing-label {
    top: 1102px;
    font-size: 17px;
    font-weight: 500;
    letter-spacing: 0.2em;
    padding-left: 0.2em;
  }
  .billing-name {
    top: 1131px;
    font-size: 31px;
    font-weight: 400;
    letter-spacing: 0.14em;
    padding-left: 0.14em;
  }
</style>
</head>
<body>
  <main class="poster">
    <p class="presenter">Velvet Harbor Pictures<br>Presents</p>
    <h1 class="title" aria-label="TINFOIL">
      <span>T</span><span>I</span><span>N</span><span>F</span><span>O</span><span>I</span><span>L</span>
    </h1>
    <svg class="emblem" viewBox="0 0 838 838" aria-hidden="true">
      <circle cx="419" cy="419" r="419"/>
    </svg>
    <p class="billing billing-label">Starring</p>
    <p class="billing billing-name">Marisa Calloway</p>
  </main>
</body>
</html>
```